New Business Card Design Project

hello again,
i have an awful year and we were not able to complete our logo plan. we would like to use our #1 logo for business card design process. the primary colors for business card should be white background with orange & black letters. our business is mobil truck cranes. we deliver heavy stuff and unload cargo with crane that is mounted on our trucks.
here is our business card info:
HARBOR LIFT HAULERS, INC.
428 WESTCOTT AVE
MERRICK, NY 11542
OFFICE - 516 487 3091
DIRECT - 1 888 LIFT HAULS
MARK@HLHAULERS.COM
PLEASE also try to get our slogan on card .... "Our Loads Keep Rollin"
lastly please also put "24 hour Knuckleboom Service"
you can call me anytime 24/7 to discuss...my cell # is: 516 759 2036
please also list: Mark Delroy, President
Target Market(s)
Heavy Construction industry
Industry/Entity Type
heavy construction industry
Contact Information for Business Card
24 Hr Knuckleboom Service

```html
<!DOCTYPE html>
<html lang="en">
<head>
<meta charset="utf-8">
<title>Harbor Lift Haulers – Business Card</title>
<link href="https://fonts.googleapis.com/css2?family=Montserrat:wght@500;600;700&family=Questrial&display=swap" rel="stylesheet">
<style>
  :root {
    --bg: #e9e9e9;
    --card: #ffffff;
    --ink: #2f2f2f;
    --ink-soft: #4a4a4a;
    --orange: #f0420f;
  }
  * { margin: 0; padding: 0; box-sizing: border-box; }
  html, body { width: 1200px; height: 1200px; overflow: hidden; background: var(--bg); }
  .canvas { position: relative; width: 1200px; height: 1200px; }
  .card {
    position: absolute; left: 262px; width: 686px; height: 391px;
    background: var(--card); border-radius: 22px;
  }
  .card--front { top: 165px; }
  .card--back { top: 653px; }

  /* front */
  .person { position: absolute; right: 371px; top: 166px; text-align: right; font-family: "Montserrat", sans-serif; }
  .person__name { font-size: 27px; font-weight: 600; color: var(--ink); letter-spacing: 0.2px; line-height: 1; }
  .person__title { font-family: "Questrial", sans-serif; font-size: 19px; color: var(--orange); margin-top: 6px; }
  .divider { position: absolute; left: 339px; top: 136px; width: 2px; height: 117px; background: var(--orange); }
  .contact { position: absolute; left: 372px; top: 130px; font-family: "Questrial", sans-serif; font-size: 19px; color: var(--ink-soft); list-style: none; }
  .contact__item { position: relative; padding-left: 20px; line-height: 23.5px; }
  .contact__item + .contact__item { margin-top: 0; }
  .contact__item--gap { margin-top: 10px; }
  .contact__icon { position: absolute; left: 0; top: 4px; width: 14px; height: 15px; fill: var(--orange); }

  /* back */
  .brand { position: absolute; left: 0; right: 0; top: 100px; text-align: center; font-family: "Montserrat", sans-serif; }
  .brand__slogan { font-size: 20px; font-weight: 600; color: var(--ink); letter-spacing: 1px; text-transform: uppercase; }
  .brand__row { display: flex; align-items: center; justify-content: center; gap: 14px; margin-top: 22px; }
  .brand__mark { width: 34px; height: 34px; border-radius: 50%; background: var(--orange); }
  .brand__name { font-size: 34px; font-weight: 700; color: var(--ink); letter-spacing: 0.5px; }
  .service { position: absolute; left: 0; right: 0; top: 320px; text-align: center; font-family: "Montserrat", sans-serif; font-size: 24px; color: var(--ink); }
  .service strong { color: var(--orange); font-weight: 700; }
  .service span { font-weight: 500; }
</style>
</head>
<body>
<main class="canvas">
  <section class="card card--front">
    <div class="person">
      <div class="person__name">MARK DELROY</div>
      <div class="person__title">President</div>
    </div>
    <div class="divider"></div>
    <ul class="contact">
      <li class="contact__item">
        <svg class="contact__icon" viewBox="0 0 14 15"><path d="M7 0a5.5 5.5 0 0 0-5.5 5.5C1.5 9.5 7 15 7 15s5.5-5.5 5.5-9.5A5.5 5.5 0 0 0 7 0zm0 7.7a2.2 2.2 0 1 1 0-4.4 2.2 2.2 0 0 1 0 4.4z"/></svg>
        428 Westcott Ave<br>Merrick, Ny 11542
      </li>
      <li class="contact__item contact__item--gap">
        <svg class="contact__icon" viewBox="0 0 14 15"><path d="M3 1l2.3 2.6-1.2 2a9 9 0 0 0 4.6 4.6l2-1.2L13 11.3 11.4 13.6C6 13.6 .9 8.6.8 3.2z"/></svg>
        516 487 3091
      </li>
      <li class="contact__item">
        <svg class="contact__icon" viewBox="0 0 14 15"><path d="M3 1l2.3 2.6-1.2 2a9 9 0 0 0 4.6 4.6l2-1.2L13 11.3 11.4 13.6C6 13.6 .9 8.6.8 3.2z"/></svg>
        1 888 LIFT
      </li>
      <li class="contact__item">
        <svg class="contact__icon" viewBox="0 0 14 15"><path d="M0 4h14v8H0z M0 4l7 5 7-5" stroke="#fff" stroke-width="1"/></svg>
        Mark@HLHaulers.Com
      </li>
    </ul>
  </section>

  <section class="card card--back">
    <div class="brand">
      <div class="brand__slogan">Our Loads Keep Rollin</div>
      <div class="brand__row">
        <div class="brand__mark"></div>
        <div class="brand__name">HARBOR LIFT HAULERS, INC.</div>
      </div>
    </div>
    <p class="service"><strong>24 hour</strong> <span>Knuckleboom</span> <strong>Service</strong></p>
  </section>
</main>
</body>
</html>
```